Banner Ads, Icons, Logos, Photos for Chamber of Commerce

We just joined a chamber of commerce. I need several items made up with our logo and branding. We do not have a copy of our logo in large format. All logo and colors can be found on our website: http://www.myridgelinerails.example

2 Banner ads – 480 pixels w x 60 pixels h and 72 dpi in jpg or png
1 Homepage ad – 600 pixels w x 100 pixels h and 72 dpi in jpg or png
1 Search Results Icon max size is 75 x 75 pixels 72 dpi in jpg or png
1 Logo max size is 150 pixels w x 100 pixels h 72 dpi in jpg or png
1 Member Page photos max size is 600 x 600 pixels 72 dpi in jpg or png.
1 Thumbnail size is 150 x 150 pixels.

Industry/Entity Type

Residential Construction

Font styles to use
Sans Serif

Colors
0392cd
34a6d7
85cae6
cfe9f4
fbf289
fbee3d
cfdeed
85acd3

Requirements
Must have
• Logo
• phone number ( 555-316-2047 )
• "Free Estimates"
Nice to have
• Fence Photos - 1 wood fence photo, 1 aluminum fence photo, 1 vinyl fence photo
Should not have
• Too many words, too many colors

```html
<!DOCTYPE html>
<html lang="en">
<head>
<meta charset="utf-8">
<title>Ridgeline Rails – Chamber Kit</title>
<link href="https://fonts.googleapis.com/css2?family=Raleway:wght@300;400;600;700;800&family=Russo+One&family=Ubuntu:wght@700&display=swap" rel="stylesheet">
<style>
  :root{
    --board:#ececec;
    --blue:#0892cf;
    --blue-soft:#cfe9f4;
    --orange:#ea9030;
    --brown:#5a3a22;
    --dark:#333333;
    --grey:#e3e3e3;
    --yellow:#f8f08a;
    --ink:#222222;
    --label:#555555;
    --white:#ffffff;
  }
  html,body{margin:0;padding:0;overflow:hidden;}
  body{width:1200px;height:1200px;background:var(--board);position:relative;font-family:"Raleway",sans-serif;}
  .label{position:absolute;font-family:"Raleway",sans-serif;font-weight:400;font-size:23px;color:var(--label);transform:translateX(-50%);white-space:nowrap;margin:0;}
  .panel{position:absolute;background:var(--white);overflow:hidden;box-shadow:0 3px 10px rgba(0,0,0,.22);}
  .panel svg{display:block;width:100%;height:100%;}
  .brand-name{font-family:"Russo One",sans-serif;fill:var(--blue);}
  .brand-phone{font-family:"Russo One",sans-serif;fill:var(--ink);}
  .brand-tag{font-family:"Raleway",sans-serif;font-weight:700;fill:var(--ink);}
  .copy{font-family:"Raleway",sans-serif;font-weight:400;fill:var(--ink);}
  .copy-strong{font-family:"Raleway",sans-serif;font-weight:700;fill:var(--ink);}
  .url{font-family:"Ubuntu",sans-serif;font-weight:700;fill:var(--brown);letter-spacing:1px;}
  .offer{font-family:"Raleway",sans-serif;font-weight:800;fill:var(--white);}
  .on-blue{fill:var(--white);}
  .thumb{position:absolute;left:665px;top:377px;width:130px;height:130px;}
  .search-icon{position:absolute;left:870px;top:350px;width:118px;height:118px;}
</style>
</head>
<body>

<p class="label" style="left:380px;top:36px;">Member Page photos 600 x 600</p>
<p class="label" style="left:830px;top:36px;">LOGO</p>
<p class="label" style="left:730px;top:336px;">Thumbnail</p>
<p class="label" style="left:933px;top:484px;">Search Results Icon</p>
<p class="label" style="left:601px;top:546px;">480 pixels w x 60 pixels Banner ads</p>
<p class="label" style="left:601px;top:921px;">Homepage ad 600 pixels x 100 pixels</p>

<!-- Member page photo -->
<div class="panel member-photo" style="left:166px;top:80px;width:427px;height:427px;">
  <svg viewBox="0 0 534 534">
    <circle cx="52" cy="150" r="265" fill="var(--blue)"/>
    <circle cx="512" cy="40" r="62" fill="var(--blue)"/>
    <circle cx="270" cy="120" r="262" fill="var(--grey)"/>
    <circle cx="0" cy="98" r="38" fill="var(--orange)"/>
    <circle cx="478" cy="41" r="16" fill="var(--orange)"/>
    <circle cx="489" cy="261" r="25" fill="var(--brown)"/>
    <circle cx="276" cy="363" r="102" fill="var(--orange)" role="img" aria-label="Portrait of the company representative"/>
    <rect x="95" y="62" width="68" height="68" fill="var(--brown)"/>
    <text class="brand-name" x="185" y="85" font-size="33">Ridgeline Rails</text>
    <text class="brand-phone" x="185" y="124" font-size="35">555-316-2047</text>
    <text class="brand-tag" x="185" y="146" font-size="12.5">“Because Good Fences Make Good Neighbors”</text>
    <text class="copy" x="276" y="207" font-size="22" text-anchor="middle">Providing Custom Fencing Solutions</text>
    <text class="copy-strong" x="276" y="236" font-size="22" text-anchor="middle">FROM OVER 30+ YEARS</text>
    <text class="url" x="267" y="512" font-size="35" text-anchor="middle">myridgelinerails.example</text>
  </svg>
</div>

<!-- Logo -->
<div class="panel logo-card" style="left:650px;top:82px;width:356px;height:237px;">
  <svg viewBox="0 0 445 297">
    <circle cx="15" cy="-42" r="121" fill="var(--blue)"/>
    <circle cx="340" cy="436" r="200" fill="var(--orange)"/>
    <rect x="42" y="120" width="60" height="60" fill="var(--brown)"/>
    <text class="brand-name" x="139" y="135" font-size="32">Ridgeline Rails</text>
    <text class="brand-phone" x="139" y="173" font-size="34">555-316-2047</text>
    <text class="brand-tag" x="139" y="195" font-size="12">“Because Good Fences Make Good Neighbors”</text>
  </svg>
</div>

<!-- Thumbnail -->
<svg class="thumb" viewBox="0 0 130 130">
  <circle cx="65" cy="65" r="64" fill="#3a3a3a" role="img" aria-label="Thumbnail portrait of the company representative"/>
</svg>

<!-- Search results icon -->
<svg class="search-icon" viewBox="0 0 118 118">
  <defs>
    <linearGradient id="icon-fill" x1="0" y1="0" x2="1" y2="1">
      <stop offset="0" stop-color="var(--blue-soft)"/><stop offset="1" stop-color="#f3d3ae"/>
    </linearGradient>
  </defs>
  <circle cx="59" cy="59" r="57" fill="url(#icon-fill)" role="img" aria-label="Search results icon artwork"/>
</svg>

<!-- Banner ad 1 -->
<div class="panel banner banner-yellow" style="left:89px;top:595px;width:1026px;height:128px;">
  <svg viewBox="0 0 1283 160">
    <defs>
      <linearGradient id="lawn" x1="0" y1="0" x2="0" y2="1">
        <stop offset="0" stop-color="#cfd8dc"/><stop offset=".45" stop-color="#e9ecea"/><stop offset=".6" stop-color="#4f8a2c"/><stop offset="1" stop-color="#2f5e1b"/>
      </linearGradient>
    </defs>
    <circle cx="0" cy="94" r="50" fill="var(--dark)"/>
    <circle cx="410" cy="156" r="28" fill="var(--blue)"/>
    <circle cx="225" cy="76" r="190" fill="var(--yellow)"/>
    <circle cx="412" cy="14" r="40" fill="var(--brown)"/>
    <circle cx="378" cy="19" r="11" fill="var(--orange)"/>
    <circle cx="1130" cy="76" r="138" fill="var(--orange)"/>
    <circle cx="1285" cy="66" r="55" fill="var(--blue)"/>
    <circle cx="930" cy="80" r="106" fill="url(#lawn)" role="img" aria-label="Black aluminum fence in front of a house"/>
    <circle cx="1030" cy="56" r="11" fill="var(--blue)"/>
    <rect x="78" y="42" width="52" height="52" fill="var(--brown)"/>
    <text class="brand-name" x="158" y="67" font-size="26">Ridgeline Rails</text>
    <text class="brand-phone" x="158" y="98" font-size="28.5">555-316-2047</text>
    <text class="brand-tag" x="158" y="117" font-size="10.5">“Because Good Fences Make Good Neighbors”</text>
    <text class="copy" x="467" y="50" font-size="24">Providing Custom Fencing</text>
    <text class="copy" x="467" y="82" font-size="24">Solutions from over 30+ years</text>
    <text class="url" x="467" y="125" font-size="27">myridgelinerails.example</text>
    <text class="offer" x="1060" y="72" font-size="29">FREE</text>
    <text class="offer" x="1060" y="104" font-size="29">ESTIMATES</text>
  </svg>
</div>

<!-- Banner ad 2 -->
<div class="panel banner banner-grey" style="left:89px;top:752px;width:1026px;height:128px;">
  <svg viewBox="0 0 1283 160">
    <defs>
      <linearGradient id="vinyl" x1="0" y1="0" x2="0" y2="1">
        <stop offset="0" stop-color="#6f9a3f"/><stop offset=".3" stop-color="#e7eef2"/><stop offset=".75" stop-color="#d9e3ea"/><stop offset="1" stop-color="#3f6e22"/>
      </linearGradient>
    </defs>
    <circle cx="0" cy="94" r="50" fill="var(--orange)"/>
    <circle cx="410" cy="160" r="28" fill="var(--brown)"/>
    <circle cx="225" cy="76" r="190" fill="var(--grey)"/>
    <circle cx="415" cy="8" r="42" fill="var(--blue)"/>
    <circle cx="378" cy="19" r="11" fill="var(--orange)"/>
    <circle cx="1130" cy="76" r="138" fill="var(--blue)"/>
    <circle cx="1285" cy="66" r="55" fill="var(--dark)"/>
    <circle cx="930" cy="80" r="106" fill="url(#vinyl)" role="img" aria-label="White vinyl privacy fence with shrubs"/>
    <circle cx="1030" cy="58" r="11" fill="var(--white)"/>
    <rect x="78" y="42" width="52" height="52" fill="var(--brown)"/>
    <text class="brand-name" x="158" y="67" font-size="26">Ridgeline Rails</text>
    <text class="brand-phone" x="158" y="98" font-size="28.5">555-316-2047</text>
    <text class="brand-tag" x="158" y="117" font-size="10.5">“Because Good Fences Make Good Neighbors”</text>
    <text class="copy" x="467" y="50" font-size="24">Providing Custom Fencing</text>
    <text class="copy" x="467" y="82" font-size="24">Solutions from over 30+ years</text>
    <text class="url" x="467" y="125" font-size="27">myridgelinerails.example</text>
    <text class="offer" x="1060" y="72" font-size="29">FREE</text>
    <text class="offer" x="1060" y="104" font-size="29">ESTIMATES</text>
  </svg>
</div>

<!-- Homepage ad -->
<div class="panel homepage-ad" style="left:87px;top:975px;width:1029px;height:171px;">
  <svg viewBox="0 0 1286 214">
    <defs>
      <linearGradient id="vinyl-wide" x1="0" y1="0" x2="0" y2="1">
        <stop offset="0" stop-color="#5f8f35"/><stop offset=".35" stop-color="#e8eff3"/><stop offset=".75" stop-color="#d6e1e8"/><stop offset="1" stop-color="#3c6a20"/>
      </linearGradient>
    </defs>
    <circle cx="141" cy="-39" r="160" fill="var(--grey)"/>
    <circle cx="43" cy="106" r="24" fill="var(--orange)"/>
    <circle cx="1056" cy="101" r="255" fill="var(--blue)"/>
    <circle cx="721" cy="111" r="160" fill="url(#vinyl-wide)" role="img" aria-label="White vinyl fence along a green yard"/>
    <circle cx="879" cy="93" r="18" fill="var(--white)"/>
    <circle cx="1241" cy="46" r="24" fill="var(--orange)"/>
    <rect x="938" y="78" width="52" height="52" fill="var(--white)"/>
    <text class="brand-name on-blue" x="1012" y="101" font-size="23">Ridgeline Rails</text>
    <text class="brand-phone on-blue" x="1012" y="130" font-size="25.5">555-316-2047</text>
    <text class="brand-tag on-blue" x="1012" y="147" font-size="9.3">“Because Good Fences Make Good Neighbors”</text>
    <text class="copy" x="97" y="69" font-size="32">Providing Custom Fencing</text>
    <text class="copy" x="97" y="111" font-size="32">Solutions from over 30+ years</text>
    <text class="url" x="97" y="167" font-size="34">myridgelinerails.example</text>
  </svg>
</div>

</body>
</html>
```